Altamira Business Card Design

The name of the business is Ruben Altamira, CPA LLC
The service that we offer is Accounting, Tax & Consulting Services. I need it to have the following items:
Ruben Altamira, Principal
Phone Number
Email Address
Physical Address

I have attached the company logo, one in black and one in white. Please provide a design in black background and the other in white background. Please include "Accounting, Tax & Consulting Services". I want the business card to be clean and very professional.

```html
<!DOCTYPE html>
<html lang="en">
<head>
<meta charset="utf-8">
<title>Ruben Altamira, CPA LLC — Business Cards</title>
<link rel="stylesheet" href="https://fonts.googleapis.com/css2?family=Montserrat:wght@500;600;700&family=Arimo:wght@400&display=swap">
<style>
  :root {
    --stage: #2a2a2a;
    --card: #0d0d0d;
    --card-edge: #161616;
    --brand-red: #9b1a1e;
    --white: #ffffff;
    --muted: #8a8a8a;
    --divider: #555555;
  }
  * { box-sizing: border-box; margin: 0; padding: 0; }
  html, body { width: 1200px; height: 900px; overflow: hidden; }
  body {
    background: var(--stage);
    display: flex;
    align-items: center;
    justify-content: center;
    gap: 40px;
  }
  .card {
    position: relative;
    width: 540px;
    height: 309px;
    background: var(--card);
    border: 1px solid var(--card-edge);
    overflow: hidden;
  }

  /* Front */
  .card-front__brand {
    position: absolute;
    left: 34px;
    top: 102px;
    width: 200px;
    display: flex;
    align-items: center;
    gap: 10px;
  }
  .brand-square {
    flex: none;
    width: 14px;
    height: 14px;
    background: var(--brand-red);
  }
  .brand-name {
    font-family: "Montserrat", sans-serif;
    font-weight: 600;
    font-size: 15px;
    letter-spacing: 0.04em;
    line-height: 1.3;
    color: var(--white);
    text-transform: uppercase;
  }
  .card-front__divider {
    position: absolute;
    left: 250px;
    top: 46px;
    width: 1px;
    height: 150px;
    background: var(--divider);
  }
  .contact {
    position: absolute;
    left: 274px;
    top: 44px;
    font-family: "Arimo", Arial, sans-serif;
    color: var(--white);
  }
  .contact__name {
    font-family: "Montserrat", sans-serif;
    font-weight: 600;
    font-size: 17px;
    color: var(--brand-red);
    text-transform: uppercase;
    letter-spacing: 0.02em;
  }
  .contact__role { font-size: 13px; margin-bottom: 14px; }
  .contact__line {
    display: flex;
    align-items: center;
    gap: 7px;
    font-size: 12.5px;
    line-height: 1.45;
  }
  .contact__icon { width: 12px; height: 12px; flex: none; }
  .contact__address { font-size: 12.5px; line-height: 1.4; margin-top: 12px; padding-left: 19px; }

  .services-band {
    position: absolute;
    left: 0;
    right: 0;
    top: 226px;
    height: 40px;
    background: var(--brand-red);
    display: flex;
    align-items: center;
    justify-content: center;
    font-family: "Montserrat", sans-serif;
    font-weight: 700;
    font-size: 14px;
    letter-spacing: 0.03em;
    color: var(--white);
    text-transform: uppercase;
  }

  /* Back */
  .card-back {
    display: flex;
    align-items: center;
    justify-content: center;
  }
  .card-back .brand-name { font-size: 21px; }
  .card-back .brand-square { width: 18px; height: 18px; }
  .card-back__brand { display: flex; align-items: center; gap: 12px; }
</style>
</head>
<body>

  <section class="card card-front" aria-label="Business card front">
    <div class="card-front__brand">
      <span class="brand-square"></span>
      <span class="brand-name">Ruben Altamira, CPA LLC</span>
    </div>

    <div class="card-front__divider"></div>

    <div class="contact">
      <p class="contact__name">Ruben Altamira</p>
      <p class="contact__role">Principal</p>
      <p class="contact__line">
        <svg class="contact__icon" viewBox="0 0 24 24" aria-hidden="true">
          <path fill="#9b1a1e" d="M6.6 10.8a15.1 15.1 0 0 0 6.6 6.6l2.2-2.2a1 1 0 0 1 1-.25 11.4 11.4 0 0 0 3.6.57 1 1 0 0 1 1 1V20a1 1 0 0 1-1 1A17 17 0 0 1 3 4a1 1 0 0 1 1-1h3.5a1 1 0 0 1 1 1c0 1.25.2 2.45.57 3.57a1 1 0 0 1-.25 1z"/>
        </svg>
        044-318 772 604
      </p>
      <p class="contact__line">
        <svg class="contact__icon" viewBox="0 0 24 24" aria-hidden="true">
          <rect x="2" y="5" width="20" height="14" fill="#9b1a1e"/>
          <path d="M2 5l10 8 10-8" fill="none" stroke="#0d0d0d" stroke-width="1.8"/>
        </svg>
        office@altamiracpa.com
      </p>
      <p class="contact__address">218, Larkspur Avenue<br>60817, Westbrook</p>
    </div>

    <div class="services-band">Accounting, Tax &amp; Consulting Services</div>
  </section>

  <section class="card card-back" aria-label="Business card back">
    <div class="card-back__brand">
      <span class="brand-square"></span>
      <span class="brand-name">Ruben Altamira, CPA LLC</span>
    </div>
  </section>

</body>
</html>
```